Album/CD cover art for album named Hollow Lanterns, by the band Velvet Meridian

I would like an album cover. The album will have a wreath of flowers similar to the first file download. In two of the flowers (white large) will the drawn faces of the two pictures attached. The bird flying out of the wreath will be a Falcon.

```html
<!DOCTYPE html>
<html lang="en">
<head>
<meta charset="utf-8">
<title>Hollow Lanterns — Velvet Meridian</title>
<link rel="stylesheet" href="https://fonts.googleapis.com/css2?family=Poppins:wght@400;700&display=swap">
<style>
  :root {
    --cover-bg: #141418;
    --title-white: #ffffff;
    --title-pink: #e9486b;
    --band-name: #f2f2f2;
    --dust: rgba(255, 255, 255, 0.18);
  }
  html, body {
    margin: 0;
    padding: 0;
    width: 1200px;
    height: 1200px;
    overflow: hidden;
    background: var(--cover-bg);
  }
  .album-cover {
    position: relative;
    width: 1200px;
    height: 1200px;
    background: var(--cover-bg);
    overflow: hidden;
  }
  .stardust-band {
    position: absolute;
    left: 0;
    top: 530px;
    width: 1200px;
    height: 90px;
    background: radial-gradient(ellipse at center, var(--dust) 0%, rgba(255,255,255,0.06) 45%, rgba(255,255,255,0) 75%);
  }
  .wreath-art {
    position: absolute;
    left: 0;
    top: 0;
    width: 1200px;
    height: 1200px;
  }
  .album-title {
    position: absolute;
    left: 0;
    width: 1200px;
    top: 500px;
    margin: 0;
    text-align: center;
    font-family: "Poppins", sans-serif;
    font-weight: 700;
    font-size: 80px;
    line-height: 108px;
    letter-spacing: 1px;
  }
  .album-title .title-line-one { display: block; color: var(--title-white); }
  .album-title .title-line-two { display: block; color: var(--title-pink); }
  .band-name {
    position: absolute;
    left: 0;
    width: 1200px;
    top: 1128px;
    margin: 0;
    text-align: center;
    font-family: "Poppins", sans-serif;
    font-weight: 400;
    font-size: 29px;
    letter-spacing: 8px;
    color: var(--band-name);
  }
</style>
</head>
<body>
  <main class="album-cover">
    <div class="stardust-band" role="img" aria-label="Faint band of scattered white sparkle dust across the middle"></div>

    <svg class="wreath-art" viewBox="0 0 1200 1200" xmlns="http://www.w3.org/2000/svg">
      <defs>
        <linearGradient id="wreathTones" x1="0" y1="0" x2="1" y2="1">
          <stop offset="0" stop-color="#e0508e"/>
          <stop offset="0.25" stop-color="#f0922e"/>
          <stop offset="0.5" stop-color="#4f7a3e"/>
          <stop offset="0.75" stop-color="#e65a9c"/>
          <stop offset="1" stop-color="#f2b634"/>
        </linearGradient>
        <linearGradient id="falconTones" x1="0" y1="0" x2="1" y2="1">
          <stop offset="0" stop-color="#6b5440"/>
          <stop offset="1" stop-color="#b98a55"/>
        </linearGradient>
      </defs>
      <g role="img" aria-label="Wreath of painted flowers in pink, orange, yellow, blue and white with green leaves, with two portraits set inside large white blossoms">
        <circle cx="600" cy="600" r="390" fill="none" stroke="url(#wreathTones)" stroke-width="230" opacity="0.85"/>
      </g>
      <g role="img" aria-label="Falcon with spread wings flying out of the wreath at upper right">
        <ellipse cx="960" cy="185" rx="190" ry="95" fill="url(#falconTones)" opacity="0.9"/>
      </g>
      <g role="img" aria-label="Falcon gliding out of the wreath at lower left">
        <ellipse cx="190" cy="1000" rx="125" ry="70" fill="url(#falconTones)" opacity="0.9"/>
      </g>
    </svg>

    <h1 class="album-title">
      <span class="title-line-one">HOLLOW</span>
      <span class="title-line-two">LANTERNS</span>
    </h1>

    <p class="band-name">Velvet Meridian</p>
  </main>
</body>
</html>
```